Plover Freightworks Business Card Design

We are a trucking and warehousing company. We run freight in the US manly from the Pacific NW to TX and back up the the PNW. We also do warehousing where we store, move, and distribute freight. Looking for a clean and modern design of business card. We would like to look rich and elegant. Attached is our logo.

Industry/Entity Type

Trucking Company

Contact Information for Business Card

Looking for a clean and modern design of business card. We would like to look rich and elegant.

Font styles to use
Sans Serif

Colors

Designer to choose colors to be used in the design.

Requirements
Must have
• logo but it should not dominate the card
Should not have
• logo should not dominate the card

```html
<!DOCTYPE html>
<html lang="en">
<head>
<meta charset="utf-8">
<title>Plover Freightworks Business Card</title>
<link rel="stylesheet" href="https://fonts.googleapis.com/css2?family=Lato:wght@400;700;900&display=swap">
<style>
  :root {
    --backdrop: #1c1c1e;
    --brand-blue: #1479c9;
    --brand-blue-deep: #0f6bb8;
    --ink: #2f3237;
    --paper: #ffffff;
    --band-dark: #3a3d42;
  }
  * { box-sizing: border-box; margin: 0; padding: 0; }
  html, body { width: 1200px; height: 900px; overflow: hidden; }
  body {
    background: var(--backdrop);
    font-family: "Lato", sans-serif;
    position: relative;
  }
  .card {
    position: absolute;
    width: 560px;
    height: 320px;
    box-shadow: 0 14px 30px rgba(0,0,0,.55);
    overflow: hidden;
  }
  /* Front */
  .card-front {
    left: 110px; top: 90px;
    background: var(--brand-blue);
    color: var(--paper);
  }
  .card-front .wordmark {
    position: absolute;
    left: 0; right: 0; top: 112px;
    text-align: center;
  }
  .wordmark-name {
    font-weight: 700;
    font-size: 40px;
    letter-spacing: 4px;
    text-transform: uppercase;
    line-height: 1;
  }
  .wordmark-dot {
    display: inline-block;
    width: 14px; height: 14px;
    border-radius: 50%;
    background: currentColor;
    margin-right: 12px;
    vertical-align: middle;
    position: relative; top: -4px;
  }
  .card-front .website {
    position: absolute;
    left: 0; right: 0; bottom: 56px;
    text-align: center;
    font-size: 12px;
    letter-spacing: 4px;
  }
  /* Back */
  .card-back {
    left: 530px; top: 480px;
    background: var(--paper);
    color: var(--ink);
  }
  .card-back .wordmark {
    position: absolute;
    left: 0; right: 0; top: 62px;
    text-align: center;
    color: var(--brand-blue);
  }
  .card-back .wordmark-name { font-size: 30px; letter-spacing: 3px; }
  .card-back .wordmark-dot { width: 11px; height: 11px; top: -3px; }
  .holder {
    position: absolute;
    right: 36px; top: 150px;
    text-align: right;
  }
  .holder-name {
    font-size: 17px;
    color: var(--brand-blue);
  }
  .holder-name strong { font-weight: 700; }
  .holder-title { font-size: 12px; margin-top: 2px; }
  .contact {
    position: absolute;
    left: 36px; bottom: 58px;
    font-size: 12px;
    line-height: 1.55;
    list-style: none;
  }
  .contact li { display: flex; align-items: flex-start; gap: 8px; }
  .contact svg { width: 12px; height: 12px; margin-top: 3px; flex: none; fill: var(--brand-blue); }
  .contact .address { color: var(--brand-blue-deep); font-weight: 700; }
  .contact .no-icon { padding-left: 20px; }
  .footer-band {
    position: absolute;
    left: 0; right: 0; bottom: 0;
    height: 24px;
    background: var(--brand-blue);
    border-top: 6px solid var(--band-dark);
  }
</style>
</head>
<body>
  <section class="card card-front">
    <div class="wordmark"><span class="wordmark-dot"></span><span class="wordmark-name">Plover Freightworks</span></div>
    <p class="website">www.ploverfreightworks.com</p>
  </section>

  <section class="card card-back">
    <div class="wordmark"><span class="wordmark-dot"></span><span class="wordmark-name">Plover Freightworks</span></div>
    <div class="holder">
      <p class="holder-name">Dana <strong>Whitfield</strong></p>
      <p class="holder-title">Chief Executive Offer</p>
    </div>
    <ul class="contact">
      <li>
        <svg viewBox="0 0 24 24" aria-hidden="true"><path d="M6.6 10.8a15.1 15.1 0 0 0 6.6 6.6l2.2-2.2c.3-.3.7-.4 1-.2 1.1.4 2.3.6 3.6.6.6 0 1 .4 1 1V20c0 .6-.4 1-1 1C10.6 21 3 13.4 3 4c0-.6.4-1 1-1h3.5c.6 0 1 .4 1 1 0 1.3.2 2.5.6 3.6.1.3 0 .7-.2 1z"/></svg>
        <span>555 014-2290</span>
      </li>
      <li class="no-icon"><span>dana@pfwmail.com</span></li>
      <li>
        <svg viewBox="0 0 24 24" aria-hidden="true"><path d="M2 5h20v14H2zm2 2v.5l8 5 8-5V7l-8 5z"/></svg>
        <span class="address">1420 Harbor View Rd<br>Suite 210, Tacoma, WA 98402</span>
      </li>
    </ul>
    <div class="footer-band"></div>
  </section>
</body>
</html>
```